Domestic Building Company requires professional webpage

We have an existing webpage that was never completed. We are a growing building company specialising in domestic building, renovations and commercial maintenance. We liaise closely with each of our clients to provide quality service they would be happy to recommend. Our easy approachable staff give our clients the confidence to discuss their needs and changes they may have along the way.
Our main source of new customers have been from recommendations of existing clients.
We would like our webpage to reflect our eye for detail and showcase our previous work.
The colour theme should be the same as the colours of our logo.
We would like the main page to really stand out with a slideshow of our pictures of works we have completed.
We would like the tabs to remain the same - Home, About Us, Our Services, Contact us.
In the Our Services section we would like each sub heading to be a link where viewers can see pictures from previous work we have completed.
Our current web page is www.kestrelbuilding.com.au

```html
<!DOCTYPE html>
<html lang="en">
<head>
<meta charset="utf-8">
<title>Kestrel Building Services</title>
<link rel="stylesheet" href="https://fonts.googleapis.com/css2?family=Open+Sans:wght@300;400;700&display=swap">
<style>
:root{
  --page:#f8f8f8;
  --text:#555555;
  --text-dark:#2e2e2e;
  --heading:#6a6a6a;
  --blue:#2677bd;
  --green:#8dc63f;
  --footer:#7dc35b;
  --white:#ffffff;
}
*{box-sizing:border-box;margin:0;padding:0}
html,body{width:936px;height:1200px;overflow:hidden}
body{background:var(--page);font-family:"Open Sans",Arial,sans-serif;color:var(--text);position:relative}
a{color:inherit;text-decoration:none}
.abs{position:absolute}

.brand{left:104px;top:30px;display:flex;align-items:center;gap:10px}
.brand-mark{width:30px;height:30px;background:var(--green)}
.brand-name{font-size:20px;font-weight:400;color:var(--blue);letter-spacing:.2px}

.main-nav{right:102px;top:43px;display:flex;gap:25px;font-size:14.5px;font-weight:400;color:var(--text-dark)}
.main-nav .active{color:var(--blue)}

.hero{left:102px;top:88px;width:732px;height:256px;
  background:linear-gradient(180deg,#c9cfd3 0%,#e6dccb 40%,#eccf9b 62%,#7a6a4f 70%,#c9a46a 78%,#e8c58c 100%)}
.hero-dots{left:447px;top:317px;display:flex;gap:1px}
.hero-dots span{width:10px;height:10px;border-radius:50%;background:var(--white)}
.hero-dots span.on{background:var(--green);border:2px solid var(--white)}

.section-title{font-size:19.5px;font-weight:300;color:var(--heading)}
.welcome-title{left:101px;top:394px}
.projects-title{left:537px;top:394px}

.welcome-photo{left:102px;top:442px;width:417px;height:170px;
  background:linear-gradient(180deg,#a9c4df 0%,#d9e3ec 45%,#8e8b82 75%,#5e5a50 100%)}
.project-photo{left:539px;top:442px;width:294px;height:198px;
  background:linear-gradient(180deg,#6f7a5a 0%,#8a6e52 40%,#7f8a5c 65%,#6f8d4a 100%)}
.slide-arrow{top:527px}
.slide-arrow.prev{left:552px}
.slide-arrow.next{left:806px}

.body-copy{font-size:11px;line-height:18.8px;font-weight:400;color:var(--text)}
.welcome-copy{left:101px;top:626px;width:410px}
.project-copy{left:540px;top:645px;width:298px}
.project-copy strong{font-weight:700;color:var(--text)}

.services-title{left:0;width:936px;top:802px;text-align:center}
.service{top:853px;width:172px}
.service-photo{width:172px;height:95px}
.service-name{display:block;margin-top:14px;font-size:11px;font-weight:700;color:var(--green);line-height:16px}
.service-text{margin-top:10px;font-size:11px;line-height:16.8px;color:var(--text-dark)}
.svc-1{left:102px}
.svc-2{left:290px}
.svc-3{left:479px}
.svc-4{left:663px}
.svc-1 .service-photo{background:linear-gradient(160deg,#3e4650 0%,#5a6470 50%,#2c3446 100%)}
.svc-2 .service-photo{background:linear-gradient(180deg,#4a5a3a 0%,#6d7a60 45%,#2a2420 100%)}
.svc-3 .service-photo{background:linear-gradient(90deg,#c9ccc8 0%,#8a5a3a 40%,#6b3e22 100%)}
.svc-4 .service-photo{background:linear-gradient(180deg,#5a5240 0%,#8a8170 35%,#f2f2f2 55%,#ffffff 100%)}
.svc-2 .service-name{margin-bottom:16px}
.svc-3 .service-name{margin-bottom:16px}
.svc-4 .service-name{margin-bottom:16px}

.site-footer{left:0;top:1117px;width:936px;height:83px;background:var(--footer);color:var(--white)}
.footer-nav{position:absolute;left:100px;top:18px;font-size:11px;display:flex;gap:12px}
.footer-nav .sep{opacity:.9}
.copyright{position:absolute;left:100px;top:46px;font-size:11px}
.social{position:absolute;left:661px;top:26px;display:flex;gap:1px}
.social span{width:34px;height:34px;border-radius:50%;background:rgba(255,255,255,.35);border:2px solid rgba(255,255,255,.8)}
</style>
</head>
<body>

<header>
  <a class="brand abs" href="#"><span class="brand-mark"></span><span class="brand-name">Kestrel Building Services</span></a>
  <nav class="main-nav abs">
    <a class="active" href="#">Home</a>
    <a href="#">About Us</a>
    <a href="#">Our Services</a>
    <a href="#">Our Projects</a>
    <a href="#">Contact us</a>
  </nav>
</header>

<div class="hero abs" role="img" aria-label="Slideshow photo of a city skyline reflected in calm water at sunset"></div>
<div class="hero-dots abs"><span class="on"></span><span></span><span></span><span></span></div>

<h2 class="section-title welcome-title abs">Welcome to&nbsp; Kestrel Building Services</h2>
<h2 class="section-title projects-title abs">Our Projects</h2>

<div class="welcome-photo abs" role="img" aria-label="Photo of a concrete building under construction with yellow tower cranes"></div>
<p class="body-copy welcome-copy abs">Kestrel Building Services Pty Ltd is a construction and renovation company that is based in the Illawarra area.&nbsp; We specialise in all areas of residential and commercial building works and aim to deliver the highest quality performance at an affordable price. We ensure our workers have undergone the qualifications and training to provide the workmanship, efficiency and reliability our clients expect. We actively engage our client from the initial greeting to the finished product, we achieve this by ensuring the clients needs remain our first priority when delivering a high quality service and product.</p>

<div class="project-photo abs" role="img" aria-label="Photo of a timber gazebo on a deck in a garden"></div>
<svg class="slide-arrow prev abs" width="14" height="22" viewBox="0 0 14 22"><path d="M11 2 L3 11 L11 20" fill="none" stroke="#fff" stroke-width="3"/></svg>
<svg class="slide-arrow next abs" width="14" height="22" viewBox="0 0 14 22"><path d="M3 2 L11 11 L3 20" fill="none" stroke="#fff" stroke-width="3"/></svg>
<p class="body-copy project-copy abs"><strong>Lorem Ipsum is simply dummy text of the printing and typesetting industry.</strong> Lorem Ipsum has been the industry's standard dummy text ever since the 1500s, when an unknown printer took a galley of type and scrambled it to make a type specimen book. It has survived not only five centuries, but also the leap into electronic typesetting, remaining essentially unchanged.</p>

<h2 class="section-title services-title abs">Our Services</h2>

<div class="service svc-1 abs">
  <div class="service-photo" role="img" aria-label="Photo of a renovated bedroom"></div>
  <a class="service-name" href="#">Residential House Extensions and Renovations</a>
  <p class="service-text">Extend and /or add on to your existing home to create modern look to your exterior and interior.</p>
</div>
<div class="service svc-2 abs">
  <div class="service-photo" role="img" aria-label="Photo of a pergola over an outdoor deck"></div>
  <a class="service-name" href="#">Pergolas</a>
  <p class="service-text">Create a functional open air outdoor room great for entertaining, improve the appearance of home and add extra space.</p>
</div>
<div class="service svc-3 abs">
  <div class="service-photo" role="img" aria-label="Photo of hardwood deck slat screening"></div>
  <a class="service-name" href="#">Decks</a>
  <p class="service-text">We create and design various shape and sized hardwood decks to cater for all styles of homes.</p>
</div>
<div class="service svc-4 abs">
  <div class="service-photo" role="img" aria-label="Photo of a white spa bath in a modern bathroom"></div>
  <a class="service-name" href="#">Bathrooms</a>
  <p class="service-text">Update and modernise existing or new bathrooms to suit your style and needs.</p>
</div>

<footer class="site-footer abs">
  <nav class="footer-nav">
    <a href="#">Home</a><span class="sep">|</span>
    <a href="#">About Us</a><span class="sep">|</span>
    <a href="#">Our Services</a><span class="sep">|</span>
    <a href="#">Our Projects</a><span class="sep">|</span>
    <a href="#">Contact us</a>
  </nav>
  <p class="copyright">© 2014 Company Name,All Rights Reserved</p>
  <div class="social" aria-label="Social links"><span></span><span></span><span></span><span></span><span></span></div>
</footer>

</body>
</html>
```